Flyer Tally Your Ledger Free

Hi
Can you please design me a DL Flyer for: Tally Your Ledger Free
Info:
Starting a new Business ?
Want to save on bookkeeping fees for your existing business?

You can now save 1000's off bookkeeping fees by Doing it Yourself.

Using our Bookkeeper software you simply key in the information as you go.

We offer one on one training, backup and support.
We can assist you with BAS Preparation and Payrol Advice.

Add Modules as required:
Point of Sale Module
Jobs Management Module
Website Intergration Module

Fee set up assistance and training.

Lets get the ball rolling: 1300 642 815
www.tylfr.com.au
admin@tylfr.com.au (use the logo thing you made)

Target Market(s)

Small Business

Colors
ec1f27
f04a50
f59296
fcdcdc
ffffff

Requirements
Nice to have
• image/s related to bookkeeping

```html
<!DOCTYPE html>
<html lang="en">
<head>
<meta charset="utf-8">
<title>Tally Your Ledger Free – DL Flyer</title>
<link href="https://fonts.googleapis.com/css2?family=Marcellus&family=Source+Serif+4:ital,wght@0,500;1,400&family=Fira+Sans:ital,wght@0,400;0,600;0,700;1,800&family=Fira+Sans+Condensed:wght@600&family=Varela+Round&family=Open+Sans:wght@400;600&display=swap" rel="stylesheet">
<style>
  :root{
    --red:#ec1f27;
    --red-soft:#f04a50;
    --pink:#f59296;
    --blush:#fcdcdc;
    --white:#ffffff;
    --ink:#1b1a1c;
    --grey:#444446;
    --stage:#c49a6e;
  }
  *{margin:0;padding:0;box-sizing:border-box}
  html,body{width:1200px;height:1125px;overflow:hidden;background:var(--stage)}
  .canvas{position:relative;width:1200px;height:1125px}

  .flyer{position:absolute;width:406px;height:861px;overflow:hidden;text-align:center}
  .flyer--back{left:218px;top:76px;background:var(--ink);color:var(--white)}
  .flyer--front{left:684px;top:80px;background:var(--white)}
  .flyer > *{position:absolute;left:0;width:100%}

  /* back side */
  .offer-heading{top:38px;font:400 31px/33px "Marcellus",serif;color:var(--red-soft);letter-spacing:.5px;
    -webkit-text-stroke:.6px var(--red-soft)}
  .assist-text{top:190px;font:500 28px/33px "Source Serif 4",serif}
  .modules{left:50px;width:303px;top:314px;height:134px;
    background:radial-gradient(ellipse at 50% 40%,#b58a57,#8d6235 90%);
    box-shadow:3px 4px 8px rgba(0,0,0,.6)}
  .modules__pill{position:absolute;left:28px;top:17px;width:251px;height:31px;border-radius:16px;
    background:linear-gradient(#f2393f,#c8141b);font:600 18px/31px "Fira Sans",sans-serif;color:var(--white);
    box-shadow:0 3px 5px rgba(0,0,0,.45)}
  .modules__list{position:absolute;left:0;width:100%;top:56px;list-style:none;
    font:600 14.5px/22px "Fira Sans",sans-serif;color:var(--white);text-shadow:0 1px 2px rgba(0,0,0,.5)}
  .cta-lead{top:461px;font:400 18px/24px "Open Sans",sans-serif}
  .cta-phone{top:484px;font:700 35px/42px "Fira Sans",sans-serif;letter-spacing:.5px}
  .rule{left:31px;width:343px;top:536px;height:4px;border-top:2px solid var(--red);border-bottom:1px solid #7a1d22}
  .website{top:549px;font:400 31px/38px "Varela Round",sans-serif;letter-spacing:.5px}
  .website b{font-weight:400;color:var(--red)}
  .email{top:598px;font:400 14px/20px "Open Sans",sans-serif;display:flex;justify-content:center;align-items:center;gap:6px}
  .books-photo{top:618px;height:243px;
    background:linear-gradient(180deg,var(--ink) 0%,#5a3b2c 35%,#d8cfc2 62%,#b9a28a 100%)}

  /* front side */
  .front-art{top:0;height:861px}
  .brand{top:51px;display:flex;justify-content:center;align-items:center;gap:10px}
  .brand__dot{width:36px;height:36px;border-radius:50%;background:var(--red)}
  .brand__name{font:600 28px/34px "Fira Sans",sans-serif;color:var(--red)}
  .question{top:126px;font:600 48px/41px "Fira Sans Condensed",sans-serif;color:var(--grey);letter-spacing:.5px}
  .how-it-works{left:81px;width:237px;top:405px;height:237px;border-radius:50%;background:var(--white);
    border:9px solid #d9d9db;box-shadow:0 4px 10px rgba(0,0,0,.3);
    display:flex;align-items:center;justify-content:center;padding-bottom:30px;
    font:600 21.5px/24.5px "Fira Sans",sans-serif;color:var(--ink)}
  .save-question{top:645px;font:italic 800 29px/35px "Fira Sans",sans-serif;color:var(--white);padding:0 8px}
  .save-note{top:763px;font:italic 400 21.5px/24.5px "Source Serif 4",serif;color:var(--blush)}
</style>
</head>
<body>
<div class="canvas">

  <section class="flyer flyer--back">
    <h2 class="offer-heading">WE OFFER ONE ON<br>ONE TRAINING,<br>BACKUP AND<br>SUPPORT.</h2>
    <p class="assist-text">We can assist you with<br>BAS Preparation and<br>Payrol Advice.</p>
    <div class="modules">
      <div class="modules__pill">Add Modules as required</div>
      <ul class="modules__list">
        <li>Point of Sale Module</li>
        <li>Jobs Management Module</li>
        <li>Website Intergration Module</li>
      </ul>
    </div>
    <p class="cta-lead">Lets get the ball rolling</p>
    <p class="cta-phone">1300 642 815</p>
    <div class="rule"></div>
    <p class="website">www.tyl<b>fr</b>.com.au</p>
    <p class="email">
      <svg width="20" height="14" viewBox="0 0 20 14" aria-hidden="true"><rect x="1" y="1" width="18" height="12" rx="1.5" fill="#f59296"/><path d="M1.5 2 10 8.5 18.5 2" fill="none" stroke="#fff" stroke-width="1.5"/></svg>
      admin@tylfr.com.au
    </p>
    <div class="books-photo" role="img" aria-label="Photo of an open book resting on a stack of books"></div>
  </section>

  <section class="flyer flyer--front">
    <svg class="front-art" width="406" height="861" viewBox="0 0 406 861">
      <defs>
        <linearGradient id="photoTone" x1="0" y1="0" x2="1" y2="0">
          <stop offset="0" stop-color="#b47a5c"/>
          <stop offset=".45" stop-color="#e9dcd3"/>
          <stop offset="1" stop-color="#c9ced6"/>
        </linearGradient>
        <linearGradient id="redTone" x1="0" y1="0" x2="1" y2="1">
          <stop offset="0" stop-color="#ec1f27"/>
          <stop offset="1" stop-color="#c9161d"/>
        </linearGradient>
      </defs>
      <rect x="0" y="212" width="406" height="440" fill="url(#photoTone)" role="img" aria-label="Photo of a smiling woman taking a file from an office shelf"/>
      <polygon points="0,405 406,620 406,861 0,861" fill="var(--pink)"/>
      <polygon points="0,418 406,633 406,861 0,861" fill="url(#redTone)"/>
    </svg>
    <div class="brand"><span class="brand__dot"></span><span class="brand__name">Tally Your Ledger Free</span></div>
    <h1 class="question">STARTING A<br>NEW BUSINESS?</h1>
    <p class="how-it-works">Using<br>our Bookkeeper<br>software you simply<br>key in the<br>information as<br>you go.</p>
    <p class="save-question">Want to save on book-<br>keeping fees for your<br>existing business?</p>
    <p class="save-note">You can now save<br>1000's off bookkeeping fees<br>by Doing it Yourself.</p>
  </section>

</div>
</body>
</html>
```